Website & Logo The full package New Business new design and idea

Word Press

Simple, clean and very professional and approachable if possible

I am looking for a full business concept from logo to colour pallet and everything in between.
Brand new business concept, the successful applicant may continue on as our outsourced point person for all future work.

I will have an animated explainer video going over the four keys to business success Staff, Product & Services, Marketing, Sales and why the need a coach just like a sporting team to stay focused and clear on measurable outcomes.

Just added script (pdf attachment) i will be using for the explainer video at top of site.
Updates

Target Market(s)

Small business owners in Australia

Industry/Entity Type

Business Consultant

Number of Pages Required

1 page

Font styles to use
Sans Serif

Colors

Designer to choose colors to be used in the design.

Requirements
Must have
• Word press using Divi platform
• Ball park as per pdf uploaded
• Must work on all devices
• Social links
• Clear and straight forward movement through site
• Great capture of name and email,
• Free Download
• 10 Things you can start today in your small business to get you going again!
Nice to have
• clean one page potentially
• Free files and resources page
Should not have
• boring old menu and old framing

```html
<!DOCTYPE html>
<html lang="en">
<head>
<meta charset="utf-8">
<title>Bright Ledger Coaching</title>
<link href="https://fonts.googleapis.com/css2?family=Montserrat:wght@400;500;600;700;800&display=swap" rel="stylesheet">
<style>
:root{
  --cyan:#1aa9d6;
  --ink:#222;
  --deep:#1d4d5a;
  --orange:#d88a1e;
  --brown:#b06f1c;
  --teal:#46beb0;
  --purple:#7a4aa0;
  --pink:#e3177a;
  --grey:#e9e9e9;
  --dark:#1f1f1f;
  --white:#fff;
}
*{margin:0;padding:0;box-sizing:border-box}
html,body{width:1200px;height:4839px;overflow:hidden}
body{font-family:'Montserrat',sans-serif;color:var(--ink);position:relative;background:var(--white)}
.abs{position:absolute}
section,header,nav,footer{position:absolute;left:0;width:1200px}
.ph{position:absolute}

/* header */
.site-header{top:0;height:135px;background:var(--white)}
.brand{left:100px;top:28px;display:flex;align-items:center;gap:12px}
.brand-dot{width:46px;height:46px;border-radius:50%;background:var(--cyan)}
.brand-name{font-weight:700;font-size:19px;color:var(--deep);line-height:1.15;width:160px}
.contact-item{top:44px;display:flex;align-items:center;gap:12px}
.contact-item .ic{width:40px;height:40px}
.contact-item b{display:block;font-size:14px;font-weight:700}
.contact-item span{font-size:11px;color:#555}

/* nav */
.main-nav{top:135px;height:49px;background:var(--cyan)}
.main-nav a{position:absolute;top:16px;color:var(--white);font-size:13px;font-weight:700;text-decoration:none;text-transform:uppercase;transform:translateX(-50%)}

/* hero */
.hero{top:184px;height:471px}
.hero .ph{inset:0;background:linear-gradient(100deg,#8a2e8a 0%,#b15a9e 40%,#d49a9a 70%,#e8c2b0 100%)}
.hero h1{left:84px;top:128px;font-size:33px;font-weight:800;color:var(--white)}
.hero p{left:84px;top:178px;width:300px;font-size:14px;font-weight:600;color:var(--white);line-height:1.5}
.btn-download{left:194px;top:277px;width:145px;height:45px;background:var(--cyan);color:var(--white);font-size:13px;font-weight:700;display:flex;align-items:center;justify-content:center;gap:8px;border-radius:3px}

/* welcome */
.welcome{top:655px;height:500px}
.sec-title{font-weight:700;font-size:32px;color:var(--deep)}
.welcome h2{left:100px;top:100px}
.welcome .lead{left:100px;top:160px;width:605px;font-size:15px;font-weight:700;line-height:1.75}
.welcome .body{left:100px;top:300px;width:605px;font-size:15px;line-height:1.75;color:#333}
.welcome .ph{left:823px;top:71px;width:242px;height:426px;background:linear-gradient(180deg,#f2f2f2,#cfd3d8 60%,#2d3440)}

/* snapshot */
.snapshot{top:1155px;height:448px;background:var(--cyan);color:var(--white)}
.snapshot h2{left:0;width:1200px;top:92px;text-align:center;font-size:32px;font-weight:700}
.snapshot .txt{left:120px;top:158px;width:960px;font-size:15px;line-height:1.6}
.snapshot h3{left:0;width:1200px;top:300px;text-align:center;font-size:28px;font-weight:700}
.band-grey{top:1603px;height:155px;background:var(--grey)}
.stat{top:1516px;width:184px;height:165px;background:#2f2f2f;border-radius:8px;color:var(--white);text-align:center;padding-top:32px;box-shadow:0 4px 10px rgba(0,0,0,.25)}
.stat b{display:block;font-size:28px;font-weight:800;margin-bottom:16px}
.stat span{font-size:13px;line-height:1.6;display:block;padding:0 18px}

/* how it works */
.how{top:1758px;height:437px}
.how .ph{left:0;top:10px;width:490px;height:352px;background:linear-gradient(135deg,#e8e8e8,#9da3aa 55%,#3a3d44)}
.how h2{left:694px;top:40px;width:400px;text-align:center;font-size:32px;font-weight:600;color:var(--deep)}
.how .sub{left:694px;top:88px;width:420px;text-align:center;font-size:14px;font-weight:700;color:var(--orange);text-transform:uppercase;line-height:1.6}
.how .body{left:694px;top:158px;width:420px;font-size:15px;line-height:1.75;color:#333}

/* pricing */
.pricing{top:2195px;height:618px}
.pricing h2{left:0;width:1200px;top:30px;text-align:center;font-size:32px;font-weight:700;color:var(--deep)}
.plan{top:102px;width:236px;height:429px;background:var(--white);border-radius:14px;box-shadow:0 2px 12px rgba(0,0,0,.18);overflow:hidden;text-align:center}
.plan .top{position:absolute;left:0;top:0;width:236px;height:170px}
.plan .top svg{position:absolute;inset:0}
.plan .lbl{position:absolute;left:22px;top:18px;font-size:15px;color:var(--white);text-align:left}
.plan .price{position:absolute;left:22px;top:44px;font-size:30px;font-weight:800;color:var(--white);text-align:left}
.plan .term{position:absolute;left:22px;top:84px;font-size:13px;color:var(--white)}
.plan h4{position:absolute;left:0;width:236px;top:182px;font-size:17px;font-weight:700}
.plan p{position:absolute;left:40px;width:156px;top:218px;font-size:11px;line-height:1.5;color:#666;text-align:left}
.plan .btn{position:absolute;left:40px;width:156px;top:374px;height:33px;border-radius:4px;color:var(--white);font-size:12px;font-weight:700;line-height:33px}

/* activate */
.activate{top:2813px;height:687px}
.activate .ph{inset:0;background:linear-gradient(160deg,#3a3a3a,#1c1c1c 50%,#2e2a26)}
.activate .intro{left:130px;width:940px;top:105px;text-align:center;font-size:15px;line-height:1.75;color:var(--white)}
.activate h2{left:0;width:1200px;top:210px;text-align:center;font-size:34px;font-weight:700;color:var(--white)}
.feature{top:290px;width:238px;height:284px;border:2px solid var(--white);color:var(--white);text-align:center}
.feature svg{position:absolute;left:79px;top:40px}
.feature p{position:absolute;left:20px;width:198px;top:170px;font-size:13px;line-height:1.7}

/* about */
.about{top:3500px;height:652px;background:var(--grey)}
.about h2{left:103px;top:100px}
.about .body{left:103px;top:172px;width:607px;font-size:15px;line-height:1.75;color:#333}
.btn-more{left:252px;top:494px;width:203px;height:64px;background:var(--brown);border:3px solid #8a5410;border-radius:6px;color:var(--white);font-weight:700;font-size:15px;display:flex;align-items:center;justify-content:center}
.about .shape{left:848px;top:307px;width:352px;height:300px}
.about .ph{left:760px;top:40px;width:310px;height:612px;background:linear-gradient(180deg,#d9d9d9,#9aa0a8 45%,#2b3a55)}

/* newsletter */
.newsletter{top:4152px;height:423px;background:var(--cyan);color:var(--white)}
.newsletter h2{left:0;width:1200px;top:100px;text-align:center;font-size:34px;font-weight:700}
.newsletter .txt{left:110px;width:980px;top:168px;text-align:center;font-size:14px;line-height:1.7}
.field{top:287px;height:58px;border:2px solid var(--white);border-radius:30px;font-size:15px;font-weight:600;display:flex;align-items:center;justify-content:center}
.submit{background:var(--white);color:var(--ink)}

/* footer */
.site-footer{top:4575px;height:264px;background:var(--dark);color:var(--white)}
.foot-contact{left:0;width:1200px;top:48px;display:flex;justify-content:center;gap:60px;font-size:15px}
.foot-contact span{display:flex;align-items:center;gap:8px}
.socials{left:0;width:1200px;top:97px;display:flex;justify-content:center;gap:14px}
.socials i{width:46px;height:46px;border-radius:50%;background:var(--white);display:block}
.foot-links{left:0;width:1200px;top:176px;text-align:center;font-size:15px;font-weight:600}
.copy{left:0;width:1200px;top:226px;text-align:center;font-size:13px;font-weight:600}
</style>
</head>
<body>

<header class="site-header">
  <div class="abs brand"><span class="brand-dot"></span><span class="brand-name">Bright Ledger Coaching</span></div>
  <div class="abs contact-item" style="left:625px">
    <svg class="ic" viewBox="0 0 40 40"><circle cx="20" cy="20" r="19" fill="#1aa9d6"/><path d="M13 11l5 1 2 6-3 2a12 12 0 0 0 6 6l2-3 6 2 1 5c-10 2-21-9-19-19z" fill="#fff"/></svg>
    <div><b>Call Us</b><span>040 555 0192</span></div>
  </div>
  <div class="abs contact-item" style="left:785px">
    <svg class="ic" viewBox="0 0 40 40"><rect x="3" y="9" width="34" height="23" rx="3" fill="#9aa3ad"/><path d="M4 11l16 12 16-12" stroke="#fff" stroke-width="2" fill="none"/></svg>
    <div><b>Contact Us</b><span>hello@brightledger.com</span></div>
  </div>
  <div class="abs contact-item" style="left:995px">
    <svg class="ic" viewBox="0 0 40 40"><path d="M20 3a12 12 0 0 0-12 12c0 9 12 22 12 22s12-13 12-22A12 12 0 0 0 20 3z" fill="#e3177a"/><circle cx="20" cy="15" r="5" fill="#fff"/></svg>
    <div><b>Visit us</b><span>12 Harbour Lane</span></div>
  </div>
</header>

<nav class="main-nav">
  <a style="left:293px">Home</a><a style="left:384px">About</a><a style="left:510px">How it works</a>
  <a style="left:648px">Application</a><a style="left:768px">Pricing</a><a style="left:884px">Contact us</a>
</nav>

<section class="hero">
  <div class="ph" role="img" aria-label="Photo of a smiling businesswoman holding a phone"></div>
  <h1 class="abs">WE PLAN YOUR SUCCESS</h1>
  <p class="abs">Read our free guide for a successful business career</p>
  <div class="abs btn-download">DOWNLOAD
    <svg width="16" height="16" viewBox="0 0 16 16"><path d="M8 2v8M4 7l4 4 4-4M2 14h12" stroke="#fff" stroke-width="2" fill="none"/></svg>
  </div>
</section>

<section class="welcome">
  <h2 class="abs sec-title">Welcome</h2>
  <p class="abs lead">Bright Ledger Coaching is here to help, support and turn your small business around. It may not be easy, it may not be pretty, it may not be conventional or what you want to hear but my only goal is to help you succeed in your small business struggling in Australia.</p>
  <p class="abs body">I offer a 12 week fully supported and personally applied program, each week you complete the activities and we meet over video call where your actions are accountable and measurable.<br>Every business and small business owner are different, so not one solution fits all and that's exactly why I can make it personal for those who want to change and need it to happen now.</p>
  <div class="ph" role="img" aria-label="Photo of a smiling man in a blazer holding a coffee cup"></div>
</section>

<section class="snapshot">
  <h2 class="abs">Australian Small Business Snapshot</h2>
  <p class="abs txt">It's an extremely sad sign of the times when you're confronted with a myriad of 'for lease' signs in shop windows along major shopping hubs.<br>While most businesses in Australia are small — accounting for 97 percent of all businesses — they're shutting their doors in alarmingly high numbers.</p>
  <h3 class="abs">What is the Small Business Failure Rate?</h3>
</section>
<div class="abs band-grey" style="left:0;width:1200px"></div>
<div class="abs stat" style="left:74px"><b>20%</b><span>of small businesses fail in their first year</span></div>
<div class="abs stat" style="left:364px"><b>30%</b><span>of small businesses fail in their second year</span></div>
<div class="abs stat" style="left:658px"><b>50%</b><span>of small businesses fail after five years in business</span></div>
<div class="abs stat" style="left:951px"><b>70%</b><span>of small business owners fail in their 10th year in business</span></div>

<section class="how">
  <div class="ph" role="img" aria-label="Photo of a business team around a table with laptops, seen from above"></div>
  <h2 class="abs">How it works</h2>
  <p class="abs sub">With your permission I breakdown your business, staff, products/services, marketing and sales.</p>
  <p class="abs body">Under each of these four key components are up to 30 or more components including your staff training and experience, business financials, public exposure and engagement with target market, current marketing and processes required to make income.</p>
</section>

<section class="pricing">
  <h2 class="abs">Let's Work Togeather</h2>
  <div class="abs plan" style="left:148px">
    <div class="top"><svg width="236" height="170"><path d="M0 0H236V110L118 160 0 110Z" fill="#46beb0"/></svg>
      <span class="lbl">Basic</span><span class="price">FREE</span></div>
    <h4>Giving Back Free</h4>
    <p>Bright Ledger Coaching is offering a FREE 12 week coaching one on one support program every 3 months to struggling businesses in 2018 as our way of giving back and helping others in need.</p>
    <div class="btn" style="background:var(--teal)">LEARN MORE</div>
  </div>
  <div class="abs plan" style="left:484px">
    <div class="top"><svg width="236" height="170"><path d="M0 0H236V110L118 160 0 110Z" fill="#7a4aa0"/></svg>
      <span class="lbl">Special Offer</span><span class="price">200$ /Week</span><span class="term">12 weeks plan</span></div>
    <h4>Special Offer</h4>
    <p>Bright Ledger Coaching is offering this incredible one on one support program to only 10 small businesses in the first quarter of 2018 at below cost, so if you need help now.</p>
    <div class="btn" style="background:var(--purple)">LEARN MORE</div>
  </div>
  <div class="abs plan" style="left:816px">
    <div class="top"><svg width="236" height="170"><path d="M0 0H236V110L118 160 0 110Z" fill="#e3177a"/></svg>
      <span class="lbl">Premium Care</span><span class="price">400$ /Week</span><span class="term">12 weeks plan</span></div>
    <h4>Limited Offer</h4>
    <p>Very limited on application only, just 4 clients per quarter. Here we provide additional one on one support each week and dive deeper into every element of your business and fast track the changes.</p>
    <div class="btn" style="background:var(--pink)">LEARN MORE</div>
  </div>
</section>

<section class="activate">
  <div class="ph" role="img" aria-label="Dark photo of people working together at a desk"></div>
  <p class="abs intro">Regardless if you're a Bright Ledger Coaching Free, Special Offer or Just a Bit More, Small Business Owner you all get one on one direct access to me each week along with mountains of accountable activities to turn your small business around into the dream you had hoped it could be.</p>
  <h2 class="abs">Activate Includes</h2>
  <div class="abs feature" style="left:94px">
    <svg width="80" height="90" viewBox="0 0 80 90"><rect x="4" y="60" width="12" height="26" fill="#fff"/><rect x="22" y="48" width="12" height="38" fill="#fff"/><rect x="40" y="36" width="12" height="50" fill="#fff"/><rect x="58" y="24" width="12" height="62" fill="#fff"/><circle cx="62" cy="12" r="11" fill="#fff"/><text x="62" y="17" text-anchor="middle" font-family="Montserrat,sans-serif" font-weight="800" font-size="14" fill="#222">$</text></svg>
    <p>Getting a measurable base line of the financials and existing marketing</p>
  </div>
  <div class="abs feature" style="left:481px">
    <svg width="80" height="90" viewBox="0 0 80 90"><rect x="26" y="6" width="50" height="40" fill="none" stroke="#fff" stroke-width="4"/><path d="M34 38l10-12 8 6 14-16" stroke="#fff" stroke-width="3" fill="none"/><circle cx="14" cy="22" r="7" fill="#fff"/><path d="M6 34h16l10 10-3 3-7-7v44h-6V64h-4v20H6z" fill="#fff"/></svg>
    <p>Discussing the past ups and downs and looking forward to the future</p>
  </div>
  <div class="abs feature" style="left:868px">
    <svg width="80" height="90" viewBox="0 0 80 90"><circle cx="38" cy="48" r="32" fill="none" stroke="#fff" stroke-width="6"/><circle cx="38" cy="48" r="19" fill="none" stroke="#fff" stroke-width="6"/><circle cx="38" cy="48" r="7" fill="#fff"/><path d="M38 48L70 14M62 10h12v12" stroke="#fff" stroke-width="5" fill="none"/></svg>
    <p>Understanding your product or service and how it fits into the current marketplace.</p>
  </div>
</section>

<section class="about">
  <h2 class="abs sec-title">About Me</h2>
  <p class="abs body">I am not superman, I just found myself absorbing information over the past 10 years through some mentors and personal development and see so many small business owners struggling and I got sick of telling myself how I would change things that I eventually approached some businesses for free and asked if they needed a hand and they were over the moon, very receptive and after a 1 hour talk the immediate action taken saw some massive returns exceeding even my estimates and now I just want to help more Small Business Owners through Bright Ledger Coaching support.</p>
  <div class="abs btn-more">READ MORE</div>
  <svg class="abs shape" viewBox="0 0 352 300"><path d="M40 40L352 0V300H0Z" fill="#c47d22"/></svg>
  <div class="ph" role="img" aria-label="Photo of a bearded man in a suit gesturing with open hands"></div>
</section>

<section class="newsletter">
  <h2 class="abs">Our Newsletter</h2>
  <p class="abs txt">Lorem ipsum dolor sit amet, consectetur adipiscing elit, sed do eiusmod tempor incididunt ut labore et dolore magna aliqua. Ut enim ad minim veniam, quis nostrud exercitation ullamco laboris nisi ut aliquip ex ea commodo consequat. Duis aute irure.</p>
  <div class="abs field" style="left:255px;width:235px">Your Name</div>
  <div class="abs field" style="left:523px;width:235px">Your e-mail</div>
  <div class="abs field submit" style="left:797px;width:151px">Submit</div>
</section>

<footer class="site-footer">
  <div class="abs foot-contact">
    <span><svg width="14" height="18" viewBox="0 0 14 18"><path d="M7 0a7 7 0 0 0-7 7c0 5 7 11 7 11s7-6 7-11a7 7 0 0 0-7-7z" fill="#fff"/><circle cx="7" cy="7" r="2.5" fill="#1f1f1f"/></svg>18 Harbour Lane Springvale</span>
    <span><svg width="16" height="16" viewBox="0 0 16 16"><path d="M2 1l4 1 1 4-2 1a8 8 0 0 0 4 4l1-2 4 1 1 4C7 15 1 9 2 1z" fill="#fff"/></svg>Phone: (555) 014-2290</span>
    <span><svg width="18" height="14" viewBox="0 0 18 14"><rect width="18" height="14" rx="2" fill="#fff"/><path d="M1 2l8 6 8-6" stroke="#1f1f1f" stroke-width="1.5" fill="none"/></svg>Email: info@brightledgercoaching.com</span>
  </div>
  <div class="abs socials"><i></i><i></i><i></i><i></i><i></i></div>
  <div class="abs foot-links">Home &nbsp;|&nbsp; About Us &nbsp;|&nbsp; How it Works &nbsp;|&nbsp; Application &nbsp;|&nbsp; Contact Us</div>
  <div class="abs copy">Copyright © 2018. All Rights Reserved.</div>
</footer>

</body>
</html>
```